Would like to get a new Ticket jacket or caddy design with a modern look for our travel company. Currently we use a one sided design. Photos attached. This ticket jacket will be used to put the domestic tickets for the resort islands and will be handed over to visitors. Free to use Maldives photos from http://bluelarkvoyage.example for ideas.

Reason: Please give 5 more days for selecting the best design and tweaking the final product

Target Market(s)

Travellers

Industry/Entity Type

Travel

Font styles to use
Sans Serif

Requirements
Must have
• Maldives photos, company addresses(Maldives and London)
Nice to have
• open to ideas
Should not have
• photos in photos or framed photos

```html
<!DOCTYPE html>
<html lang="en">
<head>
<meta charset="utf-8">
<title>Bluelark Voyage – Ticket Jacket</title>
<link rel="stylesheet" href="https://fonts.googleapis.com/css2?family=Archivo:wght@400;700&family=Cutive+Mono&display=swap">
<style>
  :root {
    --paper: #fbf1e0;
    --navy: #0f2140;
    --royal: #21508f;
    --white: #ffffff;
    --ink: #2b2f36;
    --rule: #d9605a;
    --ticket-blue: #2a63b8;
    --pocket-inside: #e9ecef;
  }
  * { margin: 0; padding: 0; box-sizing: border-box; }
  html, body { width: 1200px; height: 900px; overflow: hidden; }
  body {
    background: var(--paper);
    font-family: "Archivo", Arial, sans-serif;
    color: var(--white);
    position: relative;
  }

  /* shared */
  .panel-shadow { box-shadow: 0 6px 18px rgba(60, 40, 10, 0.2); }
  .photo { flex: 1; }
  .brand-name {
    font-size: 11px;
    font-weight: 400;
    letter-spacing: 0.06em;
    text-transform: uppercase;
    line-height: 1.25;
  }

  /* ---------- front cover ---------- */
  .cover {
    position: absolute;
    top: 40px;
    height: 290px;
    display: flex;
    overflow: hidden;
  }
  .cover--front { left: 40px; width: 540px; }
  .cover--back { left: 620px; width: 540px; }

  .brand-panel {
    width: 140px;
    background: var(--navy);
    display: flex;
    flex-direction: column;
    align-items: center;
    justify-content: center;
    gap: 12px;
    text-align: center;
  }
  .brand-dot {
    width: 40px; height: 40px;
    border-radius: 50%;
    border: 2px solid var(--white);
  }

  .photo--palm-beach {
    background:
      radial-gradient(ellipse 40% 30% at 35% 28%, rgba(120,150,60,0.55), transparent 70%),
      linear-gradient(to bottom, #143f8c 0%, #2c62ad 40%, #8fbadf 62%, #38c2c4 72%, #7fdad4 78%, #f3f1ea 84%, #ece7dc 100%);
  }
  .photo--water-villa {
    background:
      radial-gradient(ellipse 35% 40% at 80% 62%, rgba(95,62,40,0.55), transparent 70%),
      linear-gradient(to bottom, #b9c7d3 0%, #e5eaee 32%, #6fa5b0 38%, #3f8f9f 46%, #6dbab7 70%, #a6ddd6 100%);
  }
  .photo--flap-palms {
    background:
      radial-gradient(ellipse 30% 60% at 45% 30%, rgba(100,140,50,0.5), transparent 70%),
      linear-gradient(to bottom, #1b56a8 0%, #4f86c6 45%, #3cc6c4 72%, #f2f0ea 90%);
  }
  .photo--beach-panorama {
    background:
      radial-gradient(ellipse 8% 12% at 20% 44%, rgba(150,110,60,0.45), transparent 70%),
      radial-gradient(ellipse 8% 12% at 45% 42%, rgba(150,110,60,0.45), transparent 70%),
      radial-gradient(ellipse 8% 12% at 78% 44%, rgba(150,110,60,0.45), transparent 70%),
      linear-gradient(to bottom, #5f9fd8 0%, #9cc8ea 16%, #1f78b8 24%, #2ab8c6 34%, #79d7d4 40%, #f7f7f4 50%, #eeeeea 100%);
  }

  /* ---------- back cover ---------- */
  .address-panel {
    width: 230px;
    background: var(--royal);
    padding: 22px 20px;
    display: flex;
    flex-direction: column;
    gap: 12px;
  }
  .company-name {
    font-size: 16px;
    font-weight: 700;
    text-transform: uppercase;
    letter-spacing: 0.02em;
    line-height: 1.1;
  }
  .company-legal {
    display: block;
    font-size: 12px;
    font-weight: 400;
    text-transform: none;
    margin-top: 3px;
  }
  .office {
    font-size: 9px;
    line-height: 1.35;
    font-style: normal;
  }
  .office strong { font-weight: 700; }
  .office .contact { display: block; margin-top: 5px; }

  /* ---------- open jacket with insert ---------- */
  .open-jacket {
    position: absolute;
    left: 40px;
    top: 370px;
    width: 1120px;
    height: 490px;
    background: var(--pocket-inside);
    overflow: hidden;
  }
  .flap {
    position: absolute;
    left: 0; top: 0;
    width: 100%; height: 96px;
    display: flex;
  }
  .flap .brand-panel {
    width: 200px;
    flex-direction: row;
    gap: 10px;
  }
  .flap .brand-dot { width: 22px; height: 22px; border-width: 1.5px; }
  .flap .brand-name { font-size: 10px; text-align: left; }

  .ticket {
    position: absolute;
    left: 60px;
    top: 112px;
    width: 1000px;
    height: 200px;
    background: var(--white);
    border-radius: 14px;
    color: var(--ink);
    display: flex;
    box-shadow: 0 2px 6px rgba(0,0,0,0.12);
  }
  .ticket__staple {
    width: 46px;
    border-right: 1.5px dashed #b9bec6;
    display: flex;
    align-items: center;
    justify-content: center;
  }
  .ticket__staple span {
    writing-mode: vertical-rl;
    transform: rotate(180deg);
    font-size: 12px;
    line-height: 1.1;
    text-align: center;
  }
  .ticket__main {
    flex: 1;
    padding: 18px 26px;
    position: relative;
  }
  .ticket__stub {
    width: 230px;
    border-left: 1.5px dashed var(--rule);
    padding: 14px 20px;
    display: flex;
    flex-direction: column;
    align-items: center;
    gap: 8px;
  }
  .field {
    display: block;
    border-bottom: 1px solid var(--rule);
    width: 460px;
    margin-bottom: 10px;
  }
  .field__label { display: block; font-size: 9px; color: #4a4f57; }
  .field__value {
    display: block;
    font-family: "Cutive Mono", "Courier New", monospace;
    font-size: 17px;
    letter-spacing: 0.04em;
    line-height: 1.2;
  }
  .field--side {
    position: absolute;
    left: 520px;
    width: 150px;
  }
  .plane-icon { position: absolute; right: 22px; top: 14px; }
  .stub__passenger { font-size: 11px; }
  .carrier {
    width: 74px; height: 74px;
    border-radius: 50%;
    background: var(--ticket-blue);
    display: flex;
    align-items: center;
    justify-content: center;
    color: var(--white);
    font-size: 13px;
    font-weight: 700;
    letter-spacing: 0.06em;
  }
  .stub__seat { font-size: 9px; color: #4a4f57; }

  .pocket {
    position: absolute;
    left: 0; bottom: 0;
    width: 100%; height: 225px;
    box-shadow: 0 -3px 8px rgba(0,0,0,0.15);
  }
</style>
</head>
<body>

  <section class="cover cover--front panel-shadow" aria-label="Ticket jacket front">
    <div class="brand-panel">
      <span class="brand-dot" aria-hidden="true"></span>
      <span class="brand-name">Bluelark<br>Voyage</span>
    </div>
    <div class="photo photo--palm-beach" role="img"
         aria-label="Maldives beach with a leaning palm tree, wooden jetty and turquoise lagoon under a deep blue sky"></div>
  </section>

  <section class="cover cover--back panel-shadow" aria-label="Ticket jacket back">
    <div class="address-panel">
      <h1 class="company-name">Bluelark
        <span class="company-legal">Corvana Travel LTD</span>
      </h1>
      <address class="office">
        Marlow House<br>
        18 Fenwick Row<br>
        <strong>London</strong> SE9 4QT
        <span class="contact">tel: +44 20 7946 0321<br>
        fax: +44 20 7946 0388<br>
        email: info@bluelarkvoyage.example</span>
      </address>
      <address class="office">
        Ms. Ilsa Moreau<br>
        <strong>Malé</strong><br>
        Republic of Maldives
        <span class="contact">tel: +960 300 1142<br>
        fax: +960 300 1187<br>
        email: info@bluelarkvoyage.example</span>
      </address>
    </div>
    <div class="photo photo--water-villa" role="img"
         aria-label="Overwater villa deck on stilts above a clear turquoise lagoon, cloudy sky and reef waves behind"></div>
  </section>

  <section class="open-jacket panel-shadow" aria-label="Ticket jacket opened with ticket insert">
    <div class="flap">
      <div class="brand-panel">
        <span class="brand-dot" aria-hidden="true"></span>
        <span class="brand-name">Bluelark<br>Voyage</span>
      </div>
      <div class="photo photo--flap-palms" role="img"
           aria-label="Palm trees leaning over a white beach and turquoise lagoon"></div>
    </div>

    <article class="ticket" aria-label="Boarding ticket">
      <div class="ticket__staple"><span>Staple<br>Here</span></div>
      <div class="ticket__main">
        <svg class="plane-icon" width="34" height="22" viewBox="0 0 34 22" aria-hidden="true">
          <path d="M2 11 L32 9 L32 13 Z M14 10 L10 1 L14 1 L20 10 Z M14 12 L10 21 L14 21 L20 12 Z M2 11 L0 6 L3 6 L6 10 Z" fill="#c8302b"/>
        </svg>
        <div class="field">
          <span class="field__label">Class | Classe</span>
          <span class="field__value">FIRST CLASS/PREMIÈRE CLASSE</span>
        </div>
        <div class="field">
          <span class="field__label">Name | Nom</span>
          <span class="field__value">MARSH/ADELE</span>
        </div>
        <div class="field">
          <span class="field__label">Flight | Vol</span>
          <span class="field__value">BV 214</span>
        </div>
        <div class="field field--side" style="top:66px">
          <span class="field__label">Date | Date</span>
          <span class="field__value">12 MAR</span>
        </div>
        <div class="field field--side" style="top:118px">
          <span class="field__label">From | de</span>
          <span class="field__value">MALÉ</span>
        </div>
      </div>
      <div class="ticket__stub">
        <span class="stub__passenger">Passenger 1 of 1</span>
        <span class="carrier">ALDER</span>
        <span class="stub__seat">Seat | Place</span>
      </div>
    </article>

    <div class="pocket photo--beach-panorama" role="img"
         aria-label="Wide white sand beach with thatched parasols and sun loungers beside a turquoise sea"></div>
  </section>

</body>
</html>
```